Beautiful, impactful, engaging packaging for a box of a new granola brand

BL4Z™Muesli is a new brand – the packaging is one of the first touchpoints with consumers. Initially this will be in Farm Shops and Garden Centres; places where shoppers are looking for interesting new products and inspiration. We need to stand out in these busy, ‘homespun’ environments with an impactful, distinctive and engaging pack design.

The key brand communication objectives are:
o The create a unique and own-able pack design that builds a powerful Bl4z™Muesli brand
o To reflect FRESH with an ambient product in an ambient category
o To communicate our mission to create ‘an irresistible breakfast that brings families together at the breakfast table’; our passion for food and our strong natural foodie values
o To use the pack as a start point for an on-going dialogue with consumers – one that we hope will continue through social media channels (as there will be little other marketing support)

On a practical level we also need to:
o Visually disrupt the fixture providing stand-out and strong shelf blocking using the 3 variants
o Have a pack design that will work as well in Farms Shops as in mainstream grocers so that it remains constant as we develop and grow across the retail trade

Carton dimensions - height 240mm x width 160mm x depth 50mm

Target Market(s)

• 35-55-year-old busy women – pinpoint 40yrs mums
• Enjoy cooking and ideally want to make from scratch, but lack time and inspiration
• Health aware, look after themselves and choose ‘better for you’ options as a balance to their indulgences
• Like to try new things, quite experimental, especially when it comes to food. Actively seek out new food at Farmers Markets and Food Shows
• Have more time at the weekend, especially for breakfast, and want quick, convenient, healthy, delicious options to start the day
• Love spending time together as a family, really appreciate moments when everyone comes together
• Take pride in serving up delicious food; love getting positive feedback
• Delighted to find a short cut (especially undetected) and shares discoveries with friends
• Currently buy meal kits for quick evening meals and may even buy ‘Crate Chef’ or ‘Plattio’
• More likely to shop for groceries on Vendly or at Marlowes or Pennocks (or even Bovk). Likes to pop a few culinary treats into the basket.

Industry/Entity Type

Farm

Font styles to use
Sans Serif
Decorative

Requirements
Must have
• We see Bl4z™Muesli as a warm, stylish, modern, authentic brand that connects with the consumer in an emotional way. They should really feel it is a brand that speaks to them personally, one that they are proud to buy.
• Must haves:
• * BlazMuesli logo
• * 'stay blaz with us' strapline
• * 'Toasting Kit' descriptor on the front and 'Fresh Granola Toasting Kit' on the back
• * 3 step process communicated - 1. Mix 2.Toast 3. Eat
• * Show that it contains all natural ingredients - nuts, seeds, oats and honey
• * 3 colourways - one for each of the 3 variants (Mega Berrylicious, Mega Crunchy and Mega Grainy)
• * Freshness / natural cues
• *Communicate - "No artificial colours, flavours or preservatives; good source of fibre, source of protein; no refined sugar"
Nice to have
• * Should it have a picture of a bowl of granola on the front? Not sure...
• * Is there an opportunity for the design to link across the variants to create more visual impact at point of sale
Should not have
• * not too fussy or complicated - we prefer simple, bold elegance

```html
<!DOCTYPE html>
<html lang="en">
<head>
<meta charset="utf-8">
<title>BL4Z™ Muesli – Toasting Kit range</title>
<link rel="stylesheet" href="https://fonts.googleapis.com/css2?family=Fredoka:wght@500;600&family=Lobster&family=Courgette&display=swap">
<style>
  :root {
    --bg: #f4f4f6;
    --kraft: #ebe4d6;
    --teal: #2f8a84;
    --green: #86b43a;
    --plum: #7c2a7e;
    --orange: #e5891e;
    --olive: #8c8757;
    --white: #ffffff;
    --ink: #4a4038;
  }
  * { box-sizing: border-box; margin: 0; padding: 0; }
  html, body { width: 1200px; height: 1200px; overflow: hidden; background: var(--bg); }
  .range { position: relative; width: 1200px; height: 1200px; }
  .pack {
    position: absolute; top: 345px; width: 340px; height: 510px;
    overflow: hidden; box-shadow: 0 6px 18px rgba(0,0,0,0.12);
  }
  .pack--crunchy { left: 45px; --pack: var(--plum); }
  .pack--berry { left: 430px; --pack: var(--orange); }
  .pack--grainy { left: 815px; --pack: var(--olive); }
  .pack__art { position: absolute; inset: 0; }
  .brand { position: absolute; left: 44px; top: 18px; color: var(--teal); font-family: "Fredoka", sans-serif; font-weight: 600; line-height: 0.92; }
  .brand__name { font-size: 54px; letter-spacing: 1px; }
  .brand__name sup { font-size: 12px; vertical-align: 34px; font-weight: 500; }
  .brand__type { font-size: 36px; font-weight: 500; }
  .brand__tagline { display: block; margin-top: 8px; font-size: 18px; font-weight: 500; color: var(--green); }
  .variant { position: absolute; left: 42px; top: 148px; font-family: "Lobster", cursive; color: var(--pack); font-size: 26px; line-height: 0.95; }
  .pack--berry .variant { font-size: 21px; }
  .ribbon { position: absolute; left: 150px; top: 148px; width: 126px; height: 22px; }
  .ribbon__label { position: absolute; inset: 0; text-align: center; font-family: "Lobster", cursive; font-size: 14px; line-height: 22px; color: var(--white); }
  .claim { position: absolute; left: 152px; top: 176px; font-family: "Courgette", cursive; font-size: 9px; line-height: 1.15; color: var(--ink); }
  .steps { position: absolute; right: 8px; top: 18px; width: 60px; text-align: right; font-family: "Fredoka", sans-serif; font-size: 12px; color: var(--white); }
  .step { margin-bottom: 10px; }
  .step svg { display: block; margin: 3px 0 0 auto; }
  .benefits { position: absolute; left: 0; right: 0; bottom: 18px; text-align: center; font-family: "Fredoka", sans-serif; font-weight: 500; font-size: 11px; line-height: 1.3; color: var(--white); }
</style>
</head>
<body>
<main class="range">

  <section class="pack pack--crunchy" aria-label="Mega Crunchy pack front">
    <svg class="pack__art" viewBox="0 0 340 510" width="340" height="510">
      <defs>
        <radialGradient id="mix-crunchy" cx="50%" cy="50%" r="50%">
          <stop offset="0" stop-color="#b08a5c"/><stop offset="0.6" stop-color="#cdb795"/><stop offset="1" stop-color="#ebe4d6"/>
        </radialGradient>
      </defs>
      <rect width="340" height="510" fill="var(--pack)"/>
      <path d="M0 0 H270 V170 C300 260 312 350 290 400 C258 470 168 490 108 448 C58 410 22 310 0 235 Z" fill="var(--kraft)"/>
      <ellipse cx="178" cy="315" rx="122" ry="135" fill="url(#mix-crunchy)" role="img" aria-label="Walnuts, almonds, cashews and hazelnuts scattered over a leaf pattern"/>
    </svg>
    <div class="brand"><div class="brand__name">BL4Z<sup>™</sup></div><div class="brand__type">Muesli</div><span class="brand__tagline">stay blaz with us</span></div>
    <div class="variant">Mega<br>Crunchy</div>
    <div class="ribbon"><svg width="126" height="22" viewBox="0 0 126 22"><path d="M0 0 H126 L118 11 L126 22 H0 L8 11 Z" fill="var(--teal)"/></svg><span class="ribbon__label">Toasting Kit</span></div>
    <p class="claim">All natural ingredients<br>nuts, seeds, oats and honey</p>
    <div class="steps">
      <div class="step">1. Mix<svg width="14" height="14" viewBox="0 0 14 14"><path d="M3 5 A5 5 0 0 1 12 6 M11 9 A5 5 0 0 1 2 8" fill="none" stroke="#fff" stroke-width="2"/><path d="M12 2 V6 H8" fill="none" stroke="#fff" stroke-width="1.6"/></svg></div>
      <div class="step">2.Toast<svg width="12" height="16" viewBox="0 0 12 16"><path d="M6 0 C8 4 12 6 11 11 A5 5 0 0 1 1 11 C0 7 4 6 6 0 Z" fill="#fff"/></svg></div>
      <div class="step">3. Eat<svg width="18" height="16" viewBox="0 0 18 16"><circle cx="7" cy="8" r="6" fill="none" stroke="#fff" stroke-width="1.4"/><path d="M16 1 V15" stroke="#fff" stroke-width="1.6"/></svg></div>
    </div>
    <p class="benefits">No artificial colours, flavours or preservatives;<br>good source of fibre, source of protein; no refined sugar</p>
  </section>

  <section class="pack pack--berry" aria-label="Mega Berrylicious pack front">
    <svg class="pack__art" viewBox="0 0 340 510" width="340" height="510">
      <defs>
        <radialGradient id="mix-berry" cx="50%" cy="50%" r="50%">
          <stop offset="0" stop-color="#a2644a"/><stop offset="0.6" stop-color="#d2b48e"/><stop offset="1" stop-color="#ebe4d6"/>
        </radialGradient>
      </defs>
      <rect width="340" height="510" fill="var(--pack)"/>
      <path d="M0 0 H270 V170 C300 260 312 350 290 400 C258 470 168 490 108 448 C58 410 22 310 0 235 Z" fill="var(--kraft)"/>
      <ellipse cx="178" cy="315" rx="122" ry="135" fill="url(#mix-berry)" role="img" aria-label="Raisins, goji berries, dried pineapple, almonds and cashews scattered over a leaf pattern"/>
    </svg>
    <div class="brand"><div class="brand__name">BL4Z<sup>™</sup></div><div class="brand__type">Muesli</div><span class="brand__tagline">stay blaz with us</span></div>
    <div class="variant">Mega<br>Berrylicious</div>
    <div class="ribbon"><svg width="126" height="22" viewBox="0 0 126 22"><path d="M0 0 H126 L118 11 L126 22 H0 L8 11 Z" fill="var(--teal)"/></svg><span class="ribbon__label">Toasting Kit</span></div>
    <p class="claim">All natural ingredients<br>nuts, seeds, oats and honey</p>
    <div class="steps">
      <div class="step">1. Mix<svg width="14" height="14" viewBox="0 0 14 14"><path d="M3 5 A5 5 0 0 1 12 6 M11 9 A5 5 0 0 1 2 8" fill="none" stroke="#fff" stroke-width="2"/><path d="M12 2 V6 H8" fill="none" stroke="#fff" stroke-width="1.6"/></svg></div>
      <div class="step">2.Toast<svg width="12" height="16" viewBox="0 0 12 16"><path d="M6 0 C8 4 12 6 11 11 A5 5 0 0 1 1 11 C0 7 4 6 6 0 Z" fill="#fff"/></svg></div>
      <div class="step">3. Eat<svg width="18" height="16" viewBox="0 0 18 16"><circle cx="7" cy="8" r="6" fill="none" stroke="#fff" stroke-width="1.4"/><path d="M16 1 V15" stroke="#fff" stroke-width="1.6"/></svg></div>
    </div>
    <p class="benefits">No artificial colours, flavours or preservatives;<br>good source of fibre, source of protein; no refined sugar</p>
  </section>

  <section class="pack pack--grainy" aria-label="Mega Grainy pack front">
    <svg class="pack__art" viewBox="0 0 340 510" width="340" height="510">
      <defs>
        <radialGradient id="mix-grainy" cx="50%" cy="50%" r="50%">
          <stop offset="0" stop-color="#b08a5c"/><stop offset="0.6" stop-color="#cdb795"/><stop offset="1" stop-color="#ebe4d6"/>
        </radialGradient>
      </defs>
      <rect width="340" height="510" fill="var(--pack)"/>
      <path d="M0 0 H270 V170 C300 260 312 350 290 400 C258 470 168 490 108 448 C58 410 22 310 0 235 Z" fill="var(--kraft)"/>
      <ellipse cx="178" cy="315" rx="122" ry="135" fill="url(#mix-grainy)" role="img" aria-label="Walnuts, almonds, cashews and hazelnuts scattered over a leaf pattern"/>
    </svg>
    <div class="brand"><div class="brand__name">BL4Z<sup>™</sup></div><div class="brand__type">Muesli</div><span class="brand__tagline">stay blaz with us</span></div>
    <div class="variant">Mega<br>Grainy</div>
    <div class="ribbon"><svg width="126" height="22" viewBox="0 0 126 22"><path d="M0 0 H126 L118 11 L126 22 H0 L8 11 Z" fill="var(--teal)"/></svg><span class="ribbon__label">Toasting Kit</span></div>
    <p class="claim">All natural ingredients<br>nuts, seeds, oats and honey</p>
    <div class="steps">
      <div class="step">1. Mix<svg width="14" height="14" viewBox="0 0 14 14"><path d="M3 5 A5 5 0 0 1 12 6 M11 9 A5 5 0 0 1 2 8" fill="none" stroke="#fff" stroke-width="2"/><path d="M12 2 V6 H8" fill="none" stroke="#fff" stroke-width="1.6"/></svg></div>
      <div class="step">2.Toast<svg width="12" height="16" viewBox="0 0 12 16"><path d="M6 0 C8 4 12 6 11 11 A5 5 0 0 1 1 11 C0 7 4 6 6 0 Z" fill="#fff"/></svg></div>
      <div class="step">3. Eat<svg width="18" height="16" viewBox="0 0 18 16"><circle cx="7" cy="8" r="6" fill="none" stroke="#fff" stroke-width="1.4"/><path d="M16 1 V15" stroke="#fff" stroke-width="1.6"/></svg></div>
    </div>
    <p class="benefits">No artificial colours, flavours or preservatives;<br>good source of fibre, source of protein; no refined sugar</p>
  </section>

</main>
</body>
</html>
```